Webdesign for an Health & Beauty Center

We need a new modern and elegant web design for the relaunch of the http://veskarin.at/ website.
The website is for a company which offer all services for a beuty center like epilation, cosmetics and more.
The new website should use big emotional background images and a modern menu.
All in all the website should give a female expression and the design should be clear and not playful.
The existing logo used be used for the new design, the base colours of the existing website could be used optionally.

Reason: Review of the designs together with the customer needs a little more time.

Industry/Entity Type
It Company
Look and feel
Each slider illustrates characteristics of the customer's brand and the style your logo design should communicate.

```html
<!DOCTYPE html>
<html lang="de">
<head>
<meta charset="utf-8">
<title>veskarin – Health &amp; Beauty Center</title>
<link rel="stylesheet" href="https://fonts.googleapis.com/css2?family=Source+Sans+Pro:wght@300;400;600&display=swap">
<style>
  :root {
    --gold-dark: #7b602f;
    --gold-light: #cdb88f;
    --gold-text: #b3955a;
    --white: #ffffff;
    --ink: #000000;
    --grey: #8a8a8a;
    --bg-hair: #6b4434;
    --bg-skin: #c79a82;
  }
  * { margin: 0; padding: 0; box-sizing: border-box; }
  html, body { width: 1200px; height: 1044px; overflow: hidden; }
  body {
    position: relative;
    font-family: "Source Sans Pro", sans-serif;
    color: var(--white);
  }
  .backdrop {
    position: absolute; inset: 0;
    background:
      radial-gradient(ellipse 40% 30% at 50% 8%, #caa08a 0%, transparent 100%),
      radial-gradient(ellipse 60% 25% at 50% 98%, #d7b29c 0%, transparent 100%),
      linear-gradient(90deg, var(--bg-hair) 0%, #8a5a45 20%, var(--bg-skin) 50%, #8a5a45 80%, var(--bg-hair) 100%);
  }
  .page-card {
    position: absolute; left: 178px; top: 146px; width: 840px; height: 790px;
    background: var(--white); border-radius: 3px;
  }
  .brand {
    position: absolute; left: 202px; top: 168px;
    display: flex; align-items: center; gap: 8px;
  }
  .brand-dot { width: 22px; height: 22px; border-radius: 50%; background: var(--gold-light); }
  .brand-name { font-size: 40px; font-weight: 300; color: var(--gold-text); letter-spacing: 3px; line-height: 1; }
  .brand-tagline {
    position: absolute; left: 252px; top: 235px;
    font-size: 13px; letter-spacing: 1.5px; color: var(--grey); font-weight: 400;
  }
  .header-photo {
    position: absolute; left: 797px; top: 146px; width: 221px; height: 177px;
    border-top-right-radius: 3px;
    background: linear-gradient(100deg, #ffffff 0%, #f1efe9 30%, #e3e0d2 55%, #c9c3a6 75%, #8f86a0 100%);
  }
  .main-nav {
    position: absolute; left: 202px; top: 269px; width: 792px; height: 55px;
    border-radius: 3px;
    background: linear-gradient(180deg, var(--gold-dark) 0%, var(--gold-light) 100%);
    display: flex; align-items: center;
  }
  .main-nav a {
    color: var(--white); text-decoration: none; font-size: 12px; text-transform: uppercase;
    position: absolute; top: 0; line-height: 55px;
  }
  .main-nav a.active {
    left: 0; width: 81px; text-align: center; border-radius: 3px 0 0 3px;
    background: linear-gradient(180deg, #a88a55 0%, var(--gold-dark) 100%);
  }
  .hero {
    position: absolute; left: 202px; top: 339px; width: 792px; height: 309px;
    background: var(--ink); overflow: hidden;
  }
  .hero-photo {
    position: absolute; right: 0; top: 0; width: 530px; height: 100%;
    background: linear-gradient(90deg, #000 0%, #3a2418 18%, #c99478 45%, #e2b79e 65%, #efe6e0 100%);
  }
  .hero-title {
    position: absolute; left: 39px; top: 48px;
    font-size: 31px; line-height: 31px; font-weight: 300; text-transform: uppercase;
  }
  .hero-title .gold { color: var(--gold-text); }
  .hero-title strong { font-weight: 600; }
  .hero-button {
    position: absolute; left: 38px; top: 190px; width: 130px; height: 48px;
    background: linear-gradient(180deg, var(--gold-dark) 0%, var(--gold-light) 100%);
    color: var(--white); font-size: 13px; font-weight: 600; text-decoration: none;
    line-height: 48px; text-align: center;
  }
  .slider-dots { position: absolute; left: 38px; top: 255px; display: flex; gap: 8px; }
  .slider-dots span { width: 9px; height: 8px; background: var(--gold-light); }
  .slider-dots span.current { background: #3a2e1c; }
  .hero-shadow {
    position: absolute; left: 212px; top: 648px; width: 772px; height: 16px;
    background: radial-gradient(ellipse 50% 100% at 50% 0%, rgba(0,0,0,0.35), transparent 100%);
  }
  .teaser {
    position: absolute; top: 671px; height: 232px;
    background: linear-gradient(180deg, var(--gold-dark) 0%, var(--gold-light) 100%);
    padding: 20px 17px;
  }
  .teaser h2 { font-size: 26px; font-weight: 300; line-height: 1; margin-bottom: 22px; }
  .teaser p, .teaser li { font-size: 11px; line-height: 15.5px; }
  .services { left: 202px; width: 188px; }
  .services ul { list-style: none; }
  .services li { margin-bottom: 5px; }
  .contact { left: 602px; width: 200px; }
  .contact p { margin-bottom: 15px; padding-left: 2px; }
  .photo-treatment {
    position: absolute; left: 390px; top: 671px; width: 212px; height: 232px;
    background: linear-gradient(160deg, #e8e4e0 0%, #c99478 45%, #6b4434 75%, #d8c4b8 100%);
  }
  .photo-products {
    position: absolute; left: 802px; top: 671px; width: 191px; height: 232px;
    background: linear-gradient(180deg, #c9ccd0 0%, #9ea3a9 45%, #3c3f44 75%, #b9bcc0 100%);
  }
  .copyright { position: absolute; left: 179px; top: 965px; font-size: 11px; }
  .social { position: absolute; left: 892px; top: 957px; display: flex; gap: 1px; }
  .social a { width: 31px; height: 31px; border-radius: 50%; background: var(--white); display: block; }
</style>
</head>
<body>
  <div class="backdrop" role="img" aria-label="Large background photo of a woman's eyes and long auburn hair"></div>

  <div class="page-card"></div>
  <div class="header-photo" role="img" aria-label="Photo of a mortar with bath salt, yellow flowers and lavender"></div>

  <div class="brand">
    <span class="brand-dot"></span>
    <span class="brand-name">veskarin</span>
  </div>
  <div class="brand-tagline">HEALTH &amp; BEAUTY CENTER</div>

  <nav class="main-nav">
    <a class="active" href="#">Home</a>
    <a href="#" style="left:102px">About Us</a>
    <a href="#" style="left:203px">Services</a>
    <a href="#" style="left:300px">Products</a>
    <a href="#" style="left:406px">Gallery</a>
    <a href="#" style="left:499px">Contact</a>
  </nav>

  <section class="hero">
    <div class="hero-photo" role="img" aria-label="Photo of a woman receiving a relaxing facial massage"></div>
    <h1 class="hero-title">Discover master<br><span class="gold">artistry for<br>your</span><br><strong>hair at bliss</strong></h1>
    <a class="hero-button" href="#">View Our Gallery</a>
    <div class="slider-dots"><span class="current"></span><span></span><span></span></div>
  </section>
  <div class="hero-shadow"></div>

  <section class="teaser services">
    <h2>Our Services</h2>
    <ul>
      <li>Laser SHR</li>
      <li>Cavitation &amp; RF</li>
      <li>Thermo Peel</li>
      <li>Cryotherapie</li>
    </ul>
  </section>
  <div class="photo-treatment" role="img" aria-label="Photo of an ultrasonic facial skin treatment"></div>

  <section class="teaser contact">
    <h2>Contact</h2>
    <p>Lindenhofgasse 42-44<br>1100 Wien</p>
    <p>Tel. &amp; Fax: 01/ 555 27 16<br>E-Mail: info@veskarin.at</p>
    <p>Unsere Öffnungszeiten:<br>Mo - Fr: 9.00 - 19.00<br>Sa:&nbsp;&nbsp;&nbsp;&nbsp;&nbsp;&nbsp;&nbsp;10.00 - 15.00</p>
  </section>
  <div class="photo-products" role="img" aria-label="Photo of skincare cream jars and a serum bottle"></div>

  <p class="copyright">Copyright © 2014 veskarin. All rights reserved.</p>
  <div class="social">
    <a href="#" aria-label="Social network 1"></a>
    <a href="#" aria-label="Social network 2"></a>
    <a href="#" aria-label="Social network 3"></a>
    <a href="#" aria-label="Social network 4"></a>
  </div>
</body>
</html>
```